LANTERNHILL Pizza and Wraps

We need a website for a new restaurant called LANTERNHILL "PIZZA AND WRAPS".
I have attached fonts, background images, logo, images, content etc.
can provide you with what you need to get the website design done fast and easy
Updates

I have uploaded more images of the venue and some menu items. let me know if there is anything I need to provide to make your mission clear and easy

Reason: i would like a little time to provide more feedback to designers

Industry/Entity Type

Restaurant

Coding

Coded - Design and coding required

Number of Pages Required

5+ page

Colors

Designer to choose colors to be used in the design.

Requirements
Must have
• PAGES:
• Our Story
• Menu
• Reservations
• Catering & Delivery
• Contact

```html
<!DOCTYPE html>
<html lang="en">
<head>
<meta charset="utf-8">
<title>LANTERNHILL Pizza and Wraps</title>
<link href="https://fonts.googleapis.com/css2?family=Ultra&family=Roboto+Slab:wght@400;700&display=swap" rel="stylesheet">
<style>
:root{
  --red:#e5202a;
  --yellow:#f6c21a;
  --ink:#1b1b1b;
  --paper:#f3f2ef;
  --brick:#b4603f;
  --brick-dark:#8e4a30;
  --footer:#2f2f30;
  --field:#3c3c3d;
  --white:#ffffff;
  --muted:#555;
}
*{box-sizing:border-box;margin:0;padding:0}
html,body{width:1200px;height:4663px;overflow:hidden}
body{position:relative;background:var(--paper);font-family:"Roboto Slab",serif;color:var(--ink)}
.abs{position:absolute}
.display{font-family:"Ultra",serif;font-weight:400;letter-spacing:1px}
.btn{position:absolute;display:flex;align-items:center;justify-content:center;background:var(--red);color:var(--white);font-family:"Roboto Slab",serif;font-weight:700;text-transform:uppercase}

/* header */
.site-header{position:absolute;left:0;top:0;width:1200px;height:93px;background:var(--white);z-index:3}
.brand{position:absolute;left:130px;top:28px;font-family:"Ultra",serif;font-size:34px;color:var(--red)}
.topbar{position:absolute;top:14px;left:660px;font-size:13px;color:var(--muted);display:flex;gap:40px;align-items:center}
.topbar span{display:flex;gap:8px;align-items:center}
.nav{position:absolute;top:54px;left:530px;display:flex;gap:42px;font-weight:700;font-size:15px;align-items:center}
.nav .active{color:var(--red)}
.nav-cta{position:relative;background:var(--red);color:var(--white);padding:9px 20px;font-size:14px}

/* hero */
.hero-photo{left:0;top:93px;width:1200px;height:544px;background:linear-gradient(120deg,#6c4a2e 0%,#b48a5c 35%,#d8b88a 55%,#7a5535 80%,#3b2616 100%)}
.hero-sign{left:500px;top:262px;width:200px;height:56px;background:var(--yellow);color:var(--white);font-size:32px;display:flex;align-items:center;justify-content:center;transform:rotate(-2deg)}
.hero-box{left:435px;top:330px;width:336px;height:100px;border:3px solid var(--white);background:rgba(0,0,0,.25);color:var(--white);font-size:36px;display:flex;align-items:center;justify-content:center}
.hero-btn{left:513px;top:438px;width:177px;height:50px;font-size:17px}

/* about */
.about-photo{left:124px;top:730px;width:372px;height:265px;border-radius:50%;background:radial-gradient(circle,#d9c29a 0%,#c79a62 45%,#6f8d3f 70%,var(--paper) 72%)}
.about-title{left:535px;top:735px;font-size:44px}
.about-text{left:535px;top:815px;width:535px;font-size:13.5px;line-height:21px;color:#333}
.about-text p{margin-bottom:14px}
.about-btn{left:535px;top:974px;width:110px;height:38px;font-size:13px}

/* brick bands */
.brick{left:0;background:linear-gradient(180deg,var(--brick) 0%,#c0704c 50%,var(--brick-dark) 100%)}
.service-card{top:1244px;width:451px;height:366px;border:8px solid var(--white);box-shadow:0 6px 16px rgba(0,0,0,.35)}
.service-catering{left:134px;background:linear-gradient(135deg,#e9e6dd,#c9b07a 45%,#6d8b35 75%,#3a2a1c)}
.service-delivery{left:612px;background:linear-gradient(135deg,#3d7cb8,#d1b07c 50%,#bfa070)}
.service-label{position:absolute;left:0;right:0;top:126px;text-align:center;color:var(--white);font-size:40px;text-shadow:0 2px 4px rgba(0,0,0,.5)}
.service-btn{left:84px;top:188px;width:268px;height:62px;font-size:24px}
.pizza-slice{left:860px;top:1660px;width:250px;height:150px;border-radius:50% 50% 20% 20%;background:linear-gradient(160deg,#d9a44a,#c7442a 60%,#f0d68a)}

/* gallery */
.gallery-title{left:0;width:1200px;top:1828px;text-align:center;font-size:48px}
.gallery-slide{left:131px;top:1928px;width:935px;height:559px;background:linear-gradient(90deg,#2d2a25 0%,#55493c 40%,#b0684a 41%,#a85e3f 100%)}
.arrow{position:absolute;top:2158px;width:60px;height:100px;display:flex;align-items:center;justify-content:center}
.arrow-prev{left:131px;background:var(--yellow);border-radius:0 50px 50px 0}
.arrow-next{left:1006px;background:var(--red);border-radius:50px 0 0 50px}

/* menu */
.menu-title{left:0;width:1200px;top:2628px;text-align:center;font-size:48px;color:var(--ink)}
.menu-photo{box-shadow:0 6px 16px rgba(0,0,0,.35)}
.menu-card{background:var(--white);padding:34px 40px 20px 46px;box-shadow:0 6px 16px rgba(0,0,0,.35)}
.menu-card h3{font-family:"Ultra",serif;font-weight:400;font-size:30px;letter-spacing:1px;margin-bottom:20px}
.menu-item{margin-bottom:14px;width:330px}
.menu-item h4{font-size:15px;font-weight:700;margin-bottom:4px}
.menu-item p{font-size:12.5px;line-height:17px;color:#333}
.scroll-mark{position:absolute;right:22px;top:110px;width:6px;height:46px;background:var(--ink)}
.scroll-track{position:absolute;right:24px;top:110px;width:2px;height:180px;background:#ccc}

/* footer */
.site-footer{left:0;top:4244px;width:1200px;height:419px;background:var(--footer);color:var(--white)}
.footer-col{position:absolute;top:50px;text-align:center}
.footer-col h5{font-family:"Ultra",serif;font-weight:400;font-size:24px;letter-spacing:1px;margin-bottom:22px}
.footer-col p{font-size:13px;line-height:22px;color:#ddd}
.field{width:295px;height:42px;background:var(--field);margin-bottom:10px;color:#aaa;font-size:13px;padding:12px 12px}
.field.tall{height:90px}
.submit{position:relative;width:122px;height:36px;font-size:14px}
</style>
</head>
<body>

<header class="site-header">
  <div class="brand">LANTERNHILL</div>
  <div class="topbar">
    <span><svg width="14" height="14" viewBox="0 0 14 14"><circle cx="7" cy="7" r="6" fill="none" stroke="#e5202a" stroke-width="2"/><path d="M7 3v4h3" stroke="#e5202a" stroke-width="2" fill="none"/></svg>Order Foods 24/7</span>
    <span><svg width="14" height="14" viewBox="0 0 14 14"><path d="M3 1l3 3-2 2c1 2 2 3 4 4l2-2 3 3-2 2C6 13 1 8 1 3z" fill="#e5202a"/></svg>555-014-2271</span>
  </div>
  <nav class="nav">
    <span class="active">HOME</span><span>ABOUT</span><span>OUR MENU</span><span>GALLERY</span>
    <span class="nav-cta">CONTACT US</span>
  </nav>
</header>

<section class="hero">
  <div class="abs hero-photo" role="img" aria-label="Grilled pizza wraps and a cup of fries on a wooden table"></div>
  <div class="abs hero-sign display">TASTY</div>
  <div class="abs hero-box display">PIZZA WRAPS</div>
  <div class="btn hero-btn">Reserve Now</div>
</section>

<section class="about">
  <div class="abs about-photo" role="img" aria-label="Stacked pizza wraps with fresh greens"></div>
  <h2 class="abs about-title display">ABOUT US</h2>
  <div class="abs about-text">
    <p>Rich in heritage, Lanternhill is a gathering place celebrating the Mediterranean's finest fare. Lanternhill is the ultimate escape – the perfect spot to enjoy sensational food and drinks that showcases everything the Mediterranean has to offer in a single, sophisticated setting.</p>
    <p>Where an early morning walk to the bakery around the corner is a way of life, nothing beats the first loaf of bread from the oven to start your day. So we combined a variety of best ingredients and delicacies for you to enjoy that experience whenever you get the urge to do so.</p>
  </div>
  <div class="btn about-btn">Read More</div>
</section>

<section class="services">
  <div class="abs brick" style="top:1135px;width:1200px;height:622px" role="img" aria-label="Red brick wall backdrop"></div>
  <div class="abs service-card service-catering" role="img" aria-label="Catering salad platter">
    <div class="service-label display">CATERING</div>
    <div class="btn service-btn">Reserve Now</div>
  </div>
  <div class="abs service-card service-delivery" role="img" aria-label="Courier handing over delivery boxes">
    <div class="service-label display">DELIVERY</div>
    <div class="btn service-btn">Reserve Now</div>
  </div>
  <div class="abs pizza-slice" role="img" aria-label="Slice of pizza with toppings"></div>
</section>

<section class="gallery">
  <h2 class="abs gallery-title display">OUR GALLERY</h2>
  <div class="abs gallery-slide" role="img" aria-label="Restaurant entrance with brick wall and large windows"></div>
  <div class="arrow arrow-prev"><svg width="22" height="30" viewBox="0 0 22 30"><path d="M18 2L4 15l14 13" stroke="#fff" stroke-width="5" fill="none"/></svg></div>
  <div class="arrow arrow-next"><svg width="22" height="30" viewBox="0 0 22 30"><path d="M4 2l14 13L4 28" stroke="#fff" stroke-width="5" fill="none"/></svg></div>
</section>

<section class="menu">
  <div class="abs brick" style="top:2549px;width:1200px;height:1695px" role="img" aria-label="Red brick wall backdrop"></div>
  <h2 class="abs menu-title display">OUR MENU</h2>

  <div class="abs menu-photo" style="left:131px;top:2752px;width:528px;height:435px;background:linear-gradient(135deg,#5d8a2c,#c8d9a0 40%,#9a2a24 60%,#e9e3d0)" role="img" aria-label="Appetizer salad with cured meat and cheese"></div>
  <div class="abs menu-card" style="left:591px;top:2789px;width:475px;height:367px">
    <h3>APPETIZER</h3>
    <div class="menu-item"><h4>Combo Sliders</h4><p>Brisket &amp; pulled pork sliders served with all three of our BBQ sauces on the side.</p></div>
    <div class="menu-item"><h4>Mini Brisket Tacos</h4><p>Smoked brisket wrapped in a mini corn tortilla topped with pico, cheese and guac on the side.</p></div>
    <div class="menu-item"><h4>Mini Brisket Tacos</h4><p>Smoked brisket wrapped in a mini corn tortilla topped with pico, cheese and guac on the side.</p></div>
    <div class="scroll-track"></div><div class="scroll-mark"></div>
  </div>

  <div class="abs menu-photo" style="left:606px;top:3233px;width:460px;height:430px;background:linear-gradient(150deg,#f2e3c4,#c99a62 45%,#7a5a3a 80%)" role="img" aria-label="Grilled pizza wraps cut in half"></div>
  <div class="abs menu-card" style="left:134px;top:3274px;width:472px;height:364px">
    <h3>PIZZA</h3>
    <div class="menu-item"><h4>Combo Sliders</h4><p>Brisket &amp; pulled pork sliders served with all three of our BBQ sauces on the side.</p></div>
    <div class="menu-item"><h4>Mini Brisket Tacos</h4><p>Smoked brisket wrapped in a mini corn tortilla topped with pico, cheese and guac on the side.</p></div>
    <div class="menu-item"><h4>Mini Brisket Tacos</h4><p>Smoked brisket wrapped in a mini corn tortilla topped with pico, cheese and guac on the side.</p></div>
    <div class="scroll-track"></div><div class="scroll-mark"></div>
  </div>

  <div class="abs menu-photo" style="left:131px;top:3715px;width:528px;height:436px;background:linear-gradient(135deg,#e8e2d3,#d79a4e 40%,#b56f2e 65%,#5d8a4a)" role="img" aria-label="Almond tart dessert in a white dish"></div>
  <div class="abs menu-card" style="left:591px;top:3746px;width:475px;height:374px">
    <h3>DESSERTS</h3>
    <div class="menu-item"><h4>Combo Sliders</h4><p>Brisket &amp; pulled pork sliders served with all three of our BBQ sauces on the side.</p></div>
    <div class="menu-item"><h4>Mini Brisket Tacos</h4><p>Smoked brisket wrapped in a mini corn tortilla topped with pico, cheese and guac on the side.</p></div>
    <div class="menu-item"><h4>Mini Brisket Tacos</h4><p>Smoked brisket wrapped in a mini corn tortilla topped with pico, cheese and guac on the side.</p></div>
    <div class="scroll-track"></div><div class="scroll-mark"></div>
  </div>
</section>

<footer class="abs site-footer">
  <div class="footer-col" style="left:150px;width:260px">
    <h5>OUR LOCATION</h5>
    <p>118 Harbor Lane, Suite 4<br>Millbrook, open daily<br>for dine-in guests</p>
    <p style="margin-top:14px">(phone) 555-014-2271<br>(e-mail) hello@lanternhillpizza.com</p>
  </div>
  <div class="footer-col" style="left:440px;width:240px">
    <h5>WORKING HOURS</h5>
    <p>Opening Hours</p>
    <p style="margin-top:14px">Daily from noon – 10pm<br>Friday: Closed from Noon – 3pm</p>
  </div>
  <div class="footer-col" style="left:771px;width:295px;text-align:left">
    <h5 style="text-align:center">CONTACT US</h5>
    <div class="field">Name</div>
    <div class="field">Email</div>
    <div class="field">Phone</div>
    <div class="field tall">Message</div>
    <div class="btn submit">Submit</div>
  </div>
</footer>

</body>
</html>
```